Wellness, Purpose, and the Quiet Path Research Program Website

Overview: This website will serve a new research program (Wellness, Purpose, and the Quiet Path) at the Thornbury University School of Medicine. I want a clean, intuitive design that has a navigation bar, but uses icons/graphic buttons to link to the main pages. In an attached Word document, I have provided a basic information architecture for the site, understanding that this project would just generate graphics and code for the 3 pages. I highlighted the 3 pages I'd like designed.
Target market: People who want to participate in our research, or contribute grant funding to specific projects.
Number of page: The design project focuses on 3 pages, but the site must accommodate 6 pages with top-level links. See attached Word doc.
Logo and website header: Please integrate our logo in the header. I've uploaded it as a png file--both with the name of the website and with just the logo image. I imaging the logo would look great in a banner set against an image of a mountain. The two main design themes I want to see included are nature and healthcare.
Text content: I have not yet provided text. Use some dummy text.
Technical Specifications:
- Build using WordPress. We will host this site ourselves on HostBarrow using WordPress.
- The design package must be coded.
- The template must be responsive to different platforms (e.g., computer, mobile phone, Zelvo).
Thank you! I look forward to seeing your designs.
- Ned

```html
<!DOCTYPE html>
<html lang="en">
<head>
<meta charset="utf-8">
<title>Contact – Wellness, Purpose, and the Quiet Path</title>
<link href="https://fonts.googleapis.com/css2?family=Oswald:wght@400;500&family=Poppins:wght@400;500;600;700&display=swap" rel="stylesheet">
<style>
  :root{
    --blue:#0055a9;
    --blue-deep:#003f80;
    --navy:#1f4e79;
    --lime:#82ad2e;
    --teal:#1a7866;
    --leaf:#4f9d3a;
    --page:#f7f7f9;
    --ink:#1c2430;
    --muted:#66707d;
    --white:#ffffff;
    --line:rgba(255,255,255,.18);
  }
  *{box-sizing:border-box;margin:0;padding:0}
  html,body{width:1063px;height:1200px;overflow:hidden}
  body{position:relative;background:var(--page);font-family:"Poppins",sans-serif;color:var(--ink)}
  .abs{position:absolute}

  /* header */
  .site-header{position:absolute;left:0;top:0;width:1063px;height:52px;background:var(--white)}
  .brand{position:absolute;left:79px;top:8px;display:flex;align-items:center;gap:8px}
  .brand-mark{width:34px;height:34px;border-radius:50%;background:var(--leaf)}
  .brand-name{font-weight:600;font-size:9.5px;line-height:12px;color:var(--navy)}
  .main-nav{position:absolute;right:79px;top:19px;display:flex;gap:22px;font-family:"Oswald",sans-serif;font-weight:500;font-size:11.5px;letter-spacing:.8px}
  .main-nav a{color:var(--ink);text-decoration:none}
  .main-nav a.is-active{color:var(--lime)}

  /* contact */
  .contact-title{position:absolute;left:0;width:1063px;top:128px;text-align:center;font-family:"Oswald",sans-serif;font-weight:400;font-size:35px;letter-spacing:-.5px;color:var(--ink)}
  .contact-sub{position:absolute;left:0;width:1063px;top:172px;text-align:center;font-size:17px;color:var(--muted)}
  .field{position:absolute;background:var(--white);border-radius:3px;box-shadow:0 2px 10px rgba(0,0,0,.05);font-size:12.5px;color:var(--muted);padding:0 18px;display:flex;align-items:center}
  .field--message{align-items:flex-start;padding-top:12px}
  .btn-submit{position:absolute;left:467px;top:457px;width:130px;height:30px;border-radius:15px;background:var(--blue);color:var(--white);font-weight:700;font-size:12px;display:flex;align-items:center;justify-content:center}
  .info{position:absolute;top:537px;width:180px;text-align:center}
  .info-icon{width:110px;height:110px;border-radius:50%;margin:0 auto;display:flex;align-items:center;justify-content:center}
  .info-title{margin-top:16px;font-family:"Oswald",sans-serif;font-size:18px;color:var(--ink)}
  .info-text{margin-top:2px;font-size:12.5px;color:var(--muted)}

  /* footer */
  .site-footer{position:absolute;left:0;top:804px;width:1063px;height:396px;background:var(--blue);color:var(--white)}
  .footer-brand{position:absolute;left:78px;top:104px}
  .footer-brand-mark{width:110px;height:110px;border-radius:50%;background:rgba(255,255,255,.92);margin-left:40px}
  .footer-brand-name{margin-top:16px;font-weight:600;font-size:10.5px;line-height:12px}
  .footer-col{position:absolute;top:116px}
  .footer-heading{font-family:"Oswald",sans-serif;font-weight:400;font-size:19px;letter-spacing:-.3px;margin-bottom:10px}
  .footer-links{list-style:none;font-size:12.5px;line-height:23px}
  .footer-text{font-size:12.5px}
  .newsletter-input{margin-top:12px;width:198px;height:31px;border-radius:16px;background:var(--white);color:#3b4450;font-size:11px;padding:0 14px;display:flex;align-items:center}
  .btn-subscribe{margin-top:6px;width:126px;height:32px;border-radius:16px;background:var(--lime);font-family:"Oswald",sans-serif;font-weight:500;font-size:15px;letter-spacing:.8px;display:flex;align-items:center;justify-content:center}
  .contact-list{list-style:none;font-size:12.5px;line-height:23px}
  .contact-list li{display:flex;align-items:center;gap:6px}
  .socials{display:flex;gap:6px;margin-top:6px}
  .social{width:22px;height:22px;border-radius:50%;background:var(--blue-deep)}
  .map-fill{position:absolute;left:790px;top:168px;width:200px;height:110px;border-radius:30px;background:radial-gradient(rgba(255,255,255,.08),rgba(255,255,255,0) 70%)}
  .footer-rule{position:absolute;left:78px;top:354px;width:906px;height:1px;background:var(--line)}
  .copyright{position:absolute;left:0;width:1063px;top:368px;text-align:center;font-size:11px;font-weight:500}
  .to-top{position:absolute;left:1000px;top:340px;width:28px;height:28px;border-radius:50%;background:var(--lime);display:flex;align-items:center;justify-content:center}
</style>
</head>
<body>

<header class="site-header">
  <div class="brand">
    <span class="brand-mark"></span>
    <span class="brand-name">Wellness, Purpose, and the Quiet Path<br>The Research Program</span>
  </div>
  <nav class="main-nav">
    <a href="#">HOME</a><a href="#">PEOPLE</a><a href="#">PROJECTS</a><a href="#">FAQS</a><a href="#">RESOURCES</a><a href="#" class="is-active">CONTACT</a>
  </nav>
</header>

<main>
  <h1 class="contact-title">GET IN TOUCH</h1>
  <p class="contact-sub">We love to hear from you</p>

  <div class="field" style="left:259px;top:216px;width:270px;height:37px">Name</div>
  <div class="field" style="left:535px;top:216px;width:270px;height:37px">Email</div>
  <div class="field" style="left:259px;top:261px;width:270px;height:37px">Phone</div>
  <div class="field" style="left:535px;top:261px;width:270px;height:37px">Subject</div>
  <div class="field field--message" style="left:258px;top:306px;width:546px;height:139px">Message</div>
  <div class="btn-submit">SUBMIT NOW</div>

  <div class="info" style="left:251px">
    <div class="info-icon" style="background:var(--lime)">
      <svg width="30" height="40" viewBox="0 0 30 40"><path d="M15 0C6.7 0 0 6.7 0 15c0 10 15 25 15 25s15-15 15-25C30 6.7 23.3 0 15 0z" fill="#fff"/><circle cx="15" cy="14" r="5" fill="var(--lime)"/></svg>
    </div>
    <div class="info-title">ADDRESS</div>
    <div class="info-text">Some goes address</div>
  </div>
  <div class="info" style="left:441px">
    <div class="info-icon" style="background:var(--teal)">
      <svg width="40" height="30" viewBox="0 0 40 30"><rect width="40" height="30" rx="3" fill="#fff"/><path d="M2 3l18 14 18-14" fill="none" stroke="var(--teal)" stroke-width="3"/></svg>
    </div>
    <div class="info-title">EMAIL</div>
    <div class="info-text">info@email.com</div>
  </div>
  <div class="info" style="left:621px">
    <div class="info-icon" style="background:var(--leaf)">
      <svg width="38" height="38" viewBox="0 0 24 24"><path d="M6.6 10.8a15.1 15.1 0 006.6 6.6l2.2-2.2c.3-.3.7-.4 1-.2 1.1.4 2.3.6 3.6.6.6 0 1 .4 1 1V20c0 .6-.4 1-1 1C10.6 21 3 13.4 3 4c0-.6.4-1 1-1h3.5c.6 0 1 .4 1 1 0 1.3.2 2.5.6 3.6.1.3 0 .7-.2 1z" fill="#fff"/></svg>
    </div>
    <div class="info-title">PHONE</div>
    <div class="info-text">1452 565 9665</div>
  </div>
</main>

<footer class="site-footer">
  <div class="footer-brand">
    <div class="footer-brand-mark"></div>
    <div class="footer-brand-name">Wellness, Purpose, and the Quiet Path<br>The Research Program</div>
  </div>

  <div class="footer-col" style="left:366px">
    <h2 class="footer-heading">USEFUL LINKS</h2>
    <ul class="footer-links"><li>Home</li><li>People</li><li>Projects</li><li>FAQs</li><li>Resources</li><li>Contact</li></ul>
  </div>

  <div class="footer-col" style="left:547px">
    <h2 class="footer-heading">NEWSLETTER</h2>
    <p class="footer-text">Subscribe to our newsletter</p>
    <div class="newsletter-input">Email Address</div>
    <div class="btn-subscribe">SUBSCRIBE</div>
  </div>

  <div class="map-fill" role="img" aria-label="Faint dotted world map behind contact details"></div>

  <div class="footer-col" style="left:822px">
    <h2 class="footer-heading">CONTACT US</h2>
    <ul class="contact-list">
      <li><svg width="9" height="11" viewBox="0 0 30 40"><path d="M15 0C6.7 0 0 6.7 0 15c0 10 15 25 15 25s15-15 15-25C30 6.7 23.3 0 15 0z" fill="var(--lime)"/></svg>Some goes address here</li>
      <li><svg width="10" height="8" viewBox="0 0 40 30"><rect width="40" height="30" rx="3" fill="var(--lime)"/></svg>info@email.com</li>
      <li><svg width="10" height="10" viewBox="0 0 24 24"><path d="M6.6 10.8a15.1 15.1 0 006.6 6.6l2.2-2.2c.3-.3.7-.4 1-.2 1.1.4 2.3.6 3.6.6.6 0 1 .4 1 1V20c0 .6-.4 1-1 1C10.6 21 3 13.4 3 4c0-.6.4-1 1-1h3.5c.6 0 1 .4 1 1 0 1.3.2 2.5.6 3.6.1.3 0 .7-.2 1z" fill="var(--lime)"/></svg>+142 5655 555</li>
    </ul>
    <div class="socials"><span class="social"></span><span class="social"></span><span class="social"></span><span class="social"></span></div>
  </div>

  <div class="footer-rule"></div>
  <div class="copyright">Copyright 2021 | All Rights Reserved</div>
  <div class="to-top"><svg width="10" height="6" viewBox="0 0 10 6"><path d="M1 5l4-4 4 4" fill="none" stroke="#fff" stroke-width="1.6"/></svg></div>
</footer>

</body>
</html>
```